Website for "Bright Meadow Ltd" cleaning bsuiness

We require a website to expose our business to the local market. We want to provide background on who we are and what we do but in an easily digestible way. We clean domestic and commercial premises and want to provide a list of all of our services to potential customers. We operate out of Warrington in the UK.

We would like the website to be animated in some way so that the experience of using it is not dull or mundane. This website needs to be an extension of our company.

Target Market(s)

30 - 60 year olds for Domestic plus commercial clients

Industry/Entity Type

Cleaning Service

Coding

Coded - Design and coding required

Number of Pages Required

4 page

Font styles to use
Sans Serif

Colors
0455a3
3176b5
85acd3
cfdeed
ffffff
000000
1b1b1b
c8c8c8
757575

Requirements
Must have
• Logo which has been provided. Theme based around the logo and its colours. Simple layout to avoid confusion.
Nice to have
• Animations where possible to impress the customer.
Should not have
• any pictures of cleaning equipment, fairies, maids etc

```html
<!DOCTYPE html>
<html lang="en">
<head>
<meta charset="utf-8">
<title>Bright Meadow Ltd – Professional Cleaning</title>
<link rel="stylesheet" href="https://fonts.googleapis.com/css2?family=Oswald:wght@300;400;500&family=Open+Sans:wght@400;600;700&display=swap">
<style>
  :root{
    --brand:#0455a3;
    --brand-bar:#1558b0;
    --pill:rgba(38,104,214,.93);
    --white:#ffffff;
    --ink:#1b1b1b;
    --grey:#757575;
    --footer:#3a3a3a;
  }
  *{margin:0;padding:0;box-sizing:border-box}
  html,body{width:781px;height:1200px;overflow:hidden;background:var(--white)}
  body{position:relative;font-family:"Open Sans",Arial,sans-serif;color:var(--ink)}
  .abs{position:absolute;white-space:nowrap}
  a{color:inherit;text-decoration:none}

  /* top bar */
  .topbar{left:0;top:0;width:781px;height:20px;background:var(--brand-bar)}
  .top-contact{top:5px;height:10px;font-size:7.2px;line-height:10px;color:var(--white);display:flex;align-items:center;gap:5px}
  .social{top:5px;left:561px;display:flex;gap:4px}
  .social span{width:10px;height:10px;background:var(--white);opacity:.9;display:block}

  .nav-link{top:31px;font-family:"Oswald","Arial Narrow",sans-serif;font-size:11px;line-height:16px;color:var(--ink)}

  .brandbox{left:130px;top:0;width:71px;height:56px;background:var(--white);box-shadow:0 1px 4px rgba(0,0,0,.25);
    display:flex;flex-direction:column;align-items:center;justify-content:center;gap:3px;z-index:2}
  .brandbox .dot{width:9px;height:9px;border-radius:50%;background:var(--brand)}
  .brandbox .name{font-size:8px;font-weight:700;color:var(--brand);text-align:center;line-height:1.15;white-space:normal}

  /* hero */
  .hero{left:0;top:50px;width:781px;height:285px;
    background:linear-gradient(180deg,#55504a 0%,#3e3731 50%,#2a2520 100%)}
  .hero-title{left:149px;top:130px;font-family:"Oswald","Arial Narrow",sans-serif;font-weight:500;font-size:40px;line-height:44px;color:var(--white);letter-spacing:-.5px}
  .strip{left:0;top:300px;width:781px;height:35px;background:rgba(0,0,0,.6)}
  .strip-text{top:308px;font-family:"Oswald","Arial Narrow",sans-serif;font-weight:300;font-size:15.5px;line-height:20px;color:var(--white)}
  .strip-text b{font-weight:500;border-bottom:1.5px solid var(--white)}

  /* who we are */
  .section-title{font-family:"Oswald","Arial Narrow",sans-serif;font-weight:400;font-size:16px;line-height:20px;color:var(--brand)}
  .about-text{left:135px;top:399px;width:250px;white-space:normal;font-size:8px;line-height:12.2px;color:var(--ink)}
  .more{left:344px;top:495px;font-size:5.5px;line-height:8px;color:var(--ink)}
  .video{left:406px;top:374px;width:227px;height:127px;background:linear-gradient(135deg,#5c5f5c,#2e3130 60%,#3c3f3a)}
  .video-play{left:101px;top:40px}
  .video-label{left:0;top:72px;width:227px;text-align:center;color:var(--white);font-size:9.5px;line-height:12px}

  /* services */
  .services{left:0;top:537px;width:781px;height:192px;background:linear-gradient(180deg,#4b5159,#2f3338 60%,#3a3c3f)}
  .services-title{left:0;top:553px;width:781px;text-align:center;font-family:"Oswald","Arial Narrow",sans-serif;font-size:16px;line-height:22px;color:var(--white)}
  .services-title span{border-bottom:1.5px solid var(--white)}
  .pill{width:219px;height:26px;border-radius:13px;background:var(--pill);color:var(--white);font-size:10.2px;
    display:flex;align-items:center;gap:9px;padding-left:8px}
  .pill svg{flex:none}

  /* feedback */
  .feedback-title{left:0;top:760px;width:781px;text-align:center}
  .quote{left:180px;top:793px;width:421px;white-space:normal;text-align:center;font-size:8.2px;line-height:13px}
  .author{left:0;top:852px;width:781px;text-align:center;font-size:8.8px;line-height:12px;font-weight:700}

  /* contact */
  .contact-band{left:0;top:897px;width:781px;height:239px;background:linear-gradient(180deg,#2e2f31,#1e1f21 55%,#2c2d2f)}
  .contact-title{left:0;top:924px;width:781px;text-align:center;font-family:"Oswald","Arial Narrow",sans-serif;font-weight:500;font-size:16px;line-height:22px;color:var(--white)}
  .info{left:154px;font-family:"Oswald","Arial Narrow",sans-serif;font-size:11px;line-height:14px;color:var(--white)}
  .info-address{font-size:10px;line-height:12px}
  .field{left:414px;width:196px;height:30px;border-bottom:1px solid rgba(200,200,200,.5);color:#d8d8d8;font-size:9.5px;line-height:12px;padding:11px 0 0 11px}
  .send{left:460px;top:1090px;width:114px;height:20px;border-radius:10px;background:#2668d6;color:var(--white);font-size:7.5px;
    display:flex;align-items:center;justify-content:center}

  /* footer */
  .footer{left:0;top:1136px;width:781px;height:64px;background:var(--footer)}
  .footer-head{left:0;top:1146px;width:781px;text-align:center;font-family:"Oswald","Arial Narrow",sans-serif;font-weight:300;font-size:10.5px;line-height:14px;color:#9a9a9a}
  .footer-link{top:1167px;font-family:"Oswald","Arial Narrow",sans-serif;font-weight:300;font-size:8.5px;line-height:12px;color:#bdbdbd}
  .footer-copy{left:0;top:1187px;width:781px;text-align:center;font-size:5.5px;line-height:8px;color:#9a9a9a}
</style>
</head>
<body>

<div class="abs topbar"></div>
<div class="abs top-contact" style="left:304px">
  <svg width="9" height="9" viewBox="0 0 12 12"><path d="M3 1l2 2.5-1.2 1.3c.7 1.5 1.9 2.7 3.4 3.4L8.5 7 11 9l-1 2C5.5 11 1 6.5 1 2z" fill="none" stroke="#fff" stroke-width="1"/></svg>
  <span>0800 123 4567</span>
</div>
<div class="abs top-contact" style="left:406px">
  <svg width="10" height="8" viewBox="0 0 12 9"><rect x=".5" y=".5" width="11" height="8" fill="none" stroke="#fff"/><path d="M.5 .5L6 5l5.5-4.5" fill="none" stroke="#fff"/></svg>
  <span>service@brightmeadowclean.com</span>
</div>
<div class="abs social" aria-label="Social links"><span></span><span></span><span></span><span></span><span></span><span></span></div>

<nav>
  <a class="abs nav-link" style="left:316px">Who we are</a>
  <a class="abs nav-link" style="left:383px">What we offer</a>
  <a class="abs nav-link" style="left:459px">Franchisees</a>
  <a class="abs nav-link" style="left:528px">Blog</a>
  <a class="abs nav-link" style="left:568px">FAQ's</a>
  <a class="abs nav-link" style="left:613px">Contact</a>
</nav>

<div class="abs brandbox"><span class="dot"></span><span class="name">Bright Meadow<br>Ltd</span></div>

<header>
  <div class="abs hero" role="img" aria-label="Modern living room with sofa, shelving and armchair"></div>
  <h1 class="abs hero-title">We Use Environmentally<br>Responsible Cleaning Products</h1>
  <div class="abs strip"></div>
  <p class="abs strip-text" style="left:166px">GET A FREE <b>PRICE QUOTE</b></p>
  <p class="abs strip-text" style="left:345px">CALL US ON <b>0800 123 4567</b> TO GET BEST SERVICE</p>
</header>

<section>
  <h2 class="abs section-title" style="left:135px;top:375px">Who are we</h2>
  <p class="abs about-text">Lorem Ipsum is simply dummy text of the printing and typesetting industry. Lorem Ipsum has been the industry's standard dummy text ever since the 1500s, when an unknown printer took a galley of type and scrambled it to make a type specimen book. It has survived not only five centuries, but also the leap into electronic typesetting, remaining essentially unchanged.</p>
  <a class="abs more">More....</a>
  <div class="abs video" role="img" aria-label="Bright office interior with glass walls and plants">
    <svg class="abs video-play" width="25" height="25" viewBox="0 0 26 26"><circle cx="13" cy="13" r="12" fill="none" stroke="#fff" stroke-width="1.3"/><path d="M10 8l8 5-8 5z" fill="none" stroke="#fff" stroke-width="1.2"/></svg>
    <span class="abs video-label">Watch Video</span>
  </div>
</section>

<section>
  <div class="abs services" role="img" aria-label="Living room with city skyline through large windows"></div>
  <h2 class="abs services-title"><span>What we offer</span></h2>
  <div class="abs pill" style="left:154px;top:595px"><svg width="16" height="16" viewBox="0 0 16 16"><circle cx="8" cy="8" r="7" fill="none" stroke="#fff"/><path d="M8 3.8l1.2 2.6 2.8.3-2.1 1.9.6 2.8L8 10l-2.5 1.4.6-2.8L4 6.7l2.8-.3z" fill="none" stroke="#fff" stroke-width=".8"/></svg>House Cleaning</div>
  <div class="abs pill" style="left:154px;top:634px"><svg width="16" height="16" viewBox="0 0 16 16"><circle cx="8" cy="8" r="7" fill="none" stroke="#fff"/><path d="M8 3.8l1.2 2.6 2.8.3-2.1 1.9.6 2.8L8 10l-2.5 1.4.6-2.8L4 6.7l2.8-.3z" fill="none" stroke="#fff" stroke-width=".8"/></svg>Apartment Cleaning</div>
  <div class="abs pill" style="left:154px;top:673px"><svg width="16" height="16" viewBox="0 0 16 16"><circle cx="8" cy="8" r="7" fill="none" stroke="#fff"/><path d="M8 3.8l1.2 2.6 2.8.3-2.1 1.9.6 2.8L8 10l-2.5 1.4.6-2.8L4 6.7l2.8-.3z" fill="none" stroke="#fff" stroke-width=".8"/></svg>Move In/Move Out Cleaning</div>
  <div class="abs pill" style="left:406px;top:595px"><svg width="16" height="16" viewBox="0 0 16 16"><circle cx="8" cy="8" r="7" fill="none" stroke="#fff"/><path d="M8 3.8l1.2 2.6 2.8.3-2.1 1.9.6 2.8L8 10l-2.5 1.4.6-2.8L4 6.7l2.8-.3z" fill="none" stroke="#fff" stroke-width=".8"/></svg>Commercial Cleaning</div>
  <div class="abs pill" style="left:406px;top:634px"><svg width="16" height="16" viewBox="0 0 16 16"><circle cx="8" cy="8" r="7" fill="none" stroke="#fff"/><path d="M8 3.8l1.2 2.6 2.8.3-2.1 1.9.6 2.8L8 10l-2.5 1.4.6-2.8L4 6.7l2.8-.3z" fill="none" stroke="#fff" stroke-width=".8"/></svg>Green Cleaning</div>
  <div class="abs pill" style="left:406px;top:673px"><svg width="16" height="16" viewBox="0 0 16 16"><circle cx="8" cy="8" r="7" fill="none" stroke="#fff"/><path d="M8 3.8l1.2 2.6 2.8.3-2.1 1.9.6 2.8L8 10l-2.5 1.4.6-2.8L4 6.7l2.8-.3z" fill="none" stroke="#fff" stroke-width=".8"/></svg>Office Cleaning</div>
</section>

<section>
  <h2 class="abs section-title feedback-title">Customers Feedback</h2>
  <svg class="abs" style="left:146px;top:807px" width="10" height="17" viewBox="0 0 10 17"><path d="M8.5 1L1.5 8.5 8.5 16" fill="none" stroke="#555" stroke-width="1.2"/></svg>
  <svg class="abs" style="left:623px;top:807px" width="10" height="17" viewBox="0 0 10 17"><path d="M1.5 1l7 7.5-7 7.5" fill="none" stroke="#555" stroke-width="1.2"/></svg>
  <p class="abs quote">Lorem Ipsum is simply dummy text of the printing and typesetting industry. Lorem Ipsum has been the industry's standard dummy text ever since the 1500s, when an unknown printer took a galley of type and scrambled it to make a type specimen book. It has survived not only five centuries, but also the leap into electronic typesetting, remaining essentially unchanged.</p>
  <p class="abs author">Martin Hale Robson</p>
</section>

<section>
  <div class="abs contact-band" role="img" aria-label="Dim grand hall with tall arched windows and balustrade"></div>
  <h2 class="abs contact-title">Ready for a cleaner space?</h2>
  <p class="abs info" style="top:970px">Call Us - 0800 123 4567</p>
  <p class="abs info" style="top:994px">Email - Hello@brightmeadow.com</p>
  <p class="abs info info-address" style="top:1020px">Address - 27 Orchard Row WA1 2QT<br><span style="padding-left:36px">Warrington United Kingdom.</span></p>
  <div class="abs field" style="top:949px">User Name</div>
  <div class="abs field" style="top:980px">Email ID</div>
  <div class="abs field" style="top:1010px">Phone Number</div>
  <div class="abs field" style="top:1040px">Message</div>
  <div class="abs send">Send</div>
</section>

<footer>
  <div class="abs footer"></div>
  <p class="abs footer-head">QUICK LINKS</p>
  <a class="abs footer-link" style="left:263px">Who we are</a>
  <a class="abs footer-link" style="left:324px">What we offer</a>
  <a class="abs footer-link" style="left:393px">Franchisees</a>
  <a class="abs footer-link" style="left:455px">Blog</a>
  <a class="abs footer-link" style="left:492px">Contact</a>
  <p class="abs footer-copy">© Bright Meadow 2015</p>
</footer>

</body>
</html>
```